Pricing sheet For Acupuncture Clinic - Remake Attached Work

Right Now I have 4 pricing sheets that look very disorganized. They are for 4 different options of services I offer with 3 different options to pay for each service (pay each time you come in, prepaid package, or a monthly option). People get confused from this outline so looking to make this easier to understand and better looking. You can reorganize the pricing as you see fit as long as it makes sense. (ex: using columns or rows or a graph) These images are going to be made into standard sized posters (i think that is 5 feet by 7 feet?)

Instead of designing all 4 of the attached files below you can choose 1 of them to show your example of work. I will assume that style will apply to all 4 sheets if I choose your work - also need 1 sheet that can print out on paper that will show all treatments on front and back of paper.

Thank you
Mark

Target Market(s)

Spa Industry

Industry/Entity Type

Clinic

Font styles to use
Serif
Sans Serif
Decorative
Script

Colors
33a6d7
ffffff
000000

Requirements
Nice to have
• clean - organized -
Should not have
• pictures of acupuncture needles. anything sharp. anything that might make people feel afraid of getting the treatments or look painful

```html
<!DOCTYPE html>
<html lang="en">
<head>
<meta charset="utf-8">
<title>Seabright Cosmetic Acupuncture – Pricing</title>
<link href="https://fonts.googleapis.com/css2?family=Playfair+Display:wght@400;700&family=Montserrat:wght@400;500;600&family=Oswald:wght@500&display=swap" rel="stylesheet">
<style>
  :root {
    --blue: #33a6d7;
    --blue-soft: #e8f5fb;
    --white: #ffffff;
    --black: #000000;
    --ink: #111111;
    --grey: #5c5c5c;
    --line: #d6e9f2;
    --skin-light: #eedccf;
    --skin-mid: #d2b19c;
    --skin-deep: #a38573;
  }
  * { margin: 0; padding: 0; box-sizing: border-box; }
  html, body { width: 927px; height: 1200px; overflow: hidden; background: var(--white); }
  .sheet { position: relative; width: 927px; height: 1200px; background: var(--white); overflow: hidden; }

  .hero { position: absolute; left: 0; top: 0; display: block; }

  .masthead { position: absolute; left: 40px; top: 318px; width: 847px; }
  .brand-name {
    font-family: "Playfair Display", serif; font-weight: 400;
    font-size: 52px; line-height: 66px; color: var(--black);
  }
  .brand-name .accent { color: var(--blue); }
  .tagline { display: flex; align-items: center; gap: 18px; margin-top: 14px; }
  .tagline-rule { width: 220px; height: 4px; background: var(--blue); flex: none; }
  .services {
    font-family: "Montserrat", sans-serif; font-weight: 500; font-size: 13px;
    letter-spacing: 6px; color: var(--grey); white-space: nowrap;
  }

  .plans {
    position: absolute; left: 40px; top: 540px; width: 847px; height: 370px;
    display: grid; grid-template-columns: repeat(3, 1fr); gap: 18px;
  }
  .plan {
    border: 2px solid var(--line); border-top: 8px solid var(--blue);
    background: var(--white); padding: 26px 22px 22px;
    display: flex; flex-direction: column;
  }
  .plan-title {
    font-family: "Montserrat", sans-serif; font-weight: 600;
    font-size: 15px; letter-spacing: 3px; color: var(--blue);
    text-transform: uppercase; line-height: 22px; height: 44px;
  }
  .plan-rows { list-style: none; margin-top: 22px; }
  .plan-row {
    display: flex; justify-content: space-between; align-items: baseline;
    padding: 16px 0; border-bottom: 1px solid var(--line);
    font-family: "Playfair Display", serif; font-size: 16.5px; color: var(--ink);
  }
  .plan-row:last-child { border-bottom: none; }
  .plan-price { font-weight: 700; font-size: 19px; color: var(--black); letter-spacing: 1px; }

  .plan--single { background: var(--blue); border-color: var(--blue); }
  .plan--single .plan-title { color: var(--white); }
  .single-price {
    margin-top: 60px; text-align: center; color: var(--white);
    font-family: "Playfair Display", serif; font-weight: 700;
  }
  .single-amount { display: block; font-size: 84px; line-height: 90px; }
  .single-unit { display: block; font-size: 28px; line-height: 40px; }

  .terms {
    position: absolute; left: 40px; top: 934px; width: 847px; height: 196px;
    background: var(--black); color: var(--white);
    display: grid; grid-template-columns: 1fr 1fr; gap: 14px 40px;
    padding: 30px 36px; list-style: none;
    font-family: "Oswald", sans-serif; font-weight: 500;
    font-size: 17px; line-height: 26px; text-transform: uppercase; letter-spacing: 0.5px;
  }
  .term { padding-left: 18px; border-left: 3px solid var(--blue); }

  .closing-rule { position: absolute; left: 717px; top: 1160px; width: 170px; height: 4px; background: var(--blue); }
</style>
</head>
<body>
<main class="sheet">
  <svg class="hero" width="927" height="300" viewBox="0 0 927 300" role="img" aria-label="Soft-focus photo of a relaxing cosmetic acupuncture treatment">
    <defs>
      <linearGradient id="heroTone" x1="0" y1="0" x2="1" y2="1">
        <stop offset="0" stop-color="var(--skin-light)"/>
        <stop offset="0.55" stop-color="var(--skin-mid)"/>
        <stop offset="1" stop-color="var(--skin-deep)"/>
      </linearGradient>
    </defs>
    <polygon points="0,0 927,0 927,200 0,296" fill="url(#heroTone)"/>
    <polygon points="0,296 927,200 927,206 0,302" fill="var(--blue)"/>
  </svg>

  <header class="masthead">
    <h1 class="brand-name">Seabright Cosmetic<br><span class="accent">Acupuncture</span></h1>
    <div class="tagline">
      <span class="tagline-rule"></span>
      <p class="services">PAIN, WEIGHT LOSS, HORMONES, ANXIETY</p>
    </div>
  </header>

  <section class="plans">
    <article class="plan plan--single">
      <h2 class="plan-title">Pay As You Go</h2>
      <p class="single-price"><span class="single-amount">$50</span><span class="single-unit">/ Treatment</span></p>
    </article>

    <article class="plan">
      <h2 class="plan-title">Prepaid<br>Packages</h2>
      <ul class="plan-rows">
        <li class="plan-row"><span>6 Treatments</span><span class="plan-price">$270</span></li>
        <li class="plan-row"><span>12 Treatments</span><span class="plan-price">$480</span></li>
        <li class="plan-row"><span>24 Treatments</span><span class="plan-price">$720</span></li>
      </ul>
    </article>

    <article class="plan">
      <h2 class="plan-title">Monthly<br>Autopay</h2>
      <ul class="plan-rows">
        <li class="plan-row"><span>4 Treatments/Monthly</span><span class="plan-price">$160</span></li>
        <li class="plan-row"><span>8 Treatments/Monthly</span><span class="plan-price">$240</span></li>
        <li class="plan-row"><span>12 Treatments/Monthly</span><span class="plan-price">$336</span></li>
      </ul>
    </article>
  </section>

  <ul class="terms">
    <li class="term">Auto pay unused treatments roll over</li>
    <li class="term">Pre-paid package expire after 1 year</li>
    <li class="term">Auto pay may be cancelled anytime after 4 months</li>
    <li class="term">Monthly auto pay unused treatments will be forfeited 3 months after cancellation</li>
  </ul>

  <div class="closing-rule"></div>
</main>
</body>
</html>
```